Business Card Design Project

My company/business is called K-LUX Restaurant Marketing.
K-LUX = Kindle Loyalty Using eXperience (which is our tagline if you will)

Industry/Entity Type

Business

Contact Information for Business Card

The Image below is the way I want my cards to look.

A 1-sided design on clear plastic stock would be awesome
.
I don't want the "Velcor 3G" data design. Instead, replace that with "K-LUX". That way people know their business is running from K-LUX "network" (my company is called K-LUX Restaurant Marketing).

My name is Tomas Varga, and my title is "Founder & C.E.O". I want it written exactly like I just wrote it please. so that can replace the part of the image where it says "Corporate Director".

instead of the address below the Name & Title, I would like it to say
"K-LUX Restaurant Marketing" and in smaller letters below, my tagline: "Kindle Loyalty Using eXperience".

I don't need the Skype handle on there. That should free up space for my business name and tagline from above. I want the rest to stay the same, but change the information.
- Phone Number: +1 (831) 555-0148
- Email: tomas.varga1@postvale.com
- Web Address: www.kluxrestaurantmarketing.com

Finally, I want the symbols at the bottom to change. They can stay black and white, and be simple as they currently are in the picture, but I want to replace the current images with the social media symbols for Pagebloom, Picwell, Quillet, VexMo, and Streamora.

```html
<!DOCTYPE html>
<html lang="en">
<head>
<meta charset="utf-8">
<title>K-LUX Restaurant Marketing – Tomas Varga</title>
<link rel="stylesheet" href="https://fonts.googleapis.com/css2?family=Open+Sans:wght@400;600;700&display=swap">
<style>
  :root {
    --backdrop: #8d8c88;
    --card-stock: #ecebe8;
    --device-dark: #2b2b2b;
    --device-mid: #3b3b3b;
    --device-light: #8a8a8a;
    --ink: #2a2a2a;
    --accent-green: #1b9a4b;
    --white: #ffffff;
  }
  * { box-sizing: border-box; margin: 0; padding: 0; }
  html, body {
    width: 788px; height: 1200px; overflow: hidden;
    background: var(--backdrop);
    font-family: "Open Sans", Arial, sans-serif;
    color: var(--ink);
  }
  .card {
    position: absolute; left: 64px; top: 24px;
    width: 600px; height: 1047px;
    background: var(--card-stock);
    transform: scale(1.1); transform-origin: 0 0;
  }
  .earpiece-bar, .home-bar {
    position: absolute; left: 47px; width: 506px; height: 128px;
    background: var(--device-dark); border-radius: 12px;
  }
  .earpiece-bar { top: 44px; }
  .home-bar { top: 873px; }
  .camera-dot {
    position: absolute; left: 119px; top: 52px; width: 24px; height: 24px;
    border-radius: 50%; background: var(--device-mid);
  }
  .camera-dot::after {
    content: ""; position: absolute; left: 9px; top: 9px; width: 6px; height: 6px;
    border-radius: 50%; background: #222;
  }
  .speaker-grille {
    position: absolute; left: 187px; top: 51px; width: 132px; height: 26px;
    border-radius: 13px; background: var(--device-mid);
  }
  .speaker-grille::after {
    content: ""; position: absolute; left: 8px; top: 7px; right: 8px; bottom: 7px;
    border-radius: 6px; background: #4a4a4a;
  }
  .home-button {
    position: absolute; left: 212px; top: 24px; width: 80px; height: 80px;
    border-radius: 50%; background: var(--device-mid);
  }
  .home-button::after {
    content: ""; position: absolute; left: 23px; top: 23px; width: 34px; height: 34px;
    border: 2px solid var(--device-light); border-radius: 8px;
  }
  .status-bar {
    position: absolute; left: 49px; right: 47px; top: 190px; height: 30px;
    font-weight: 700; font-size: 23px; line-height: 30px;
  }
  .status-network { position: absolute; left: 0; display: flex; align-items: center; gap: 6px; }
  .status-time { position: absolute; left: 0; right: 0; text-align: center; }
  .status-battery { position: absolute; right: 0; display: flex; align-items: center; gap: 3px; }
  .holder-name {
    position: absolute; left: 0; right: 0; top: 274px; text-align: center;
    font-size: 45px; font-weight: 700; line-height: 60px;
  }
  .holder-title {
    position: absolute; left: 0; right: 0; top: 338px; text-align: center;
    font-size: 23px; line-height: 30px;
  }
  .company-name {
    position: absolute; left: 136px; top: 403px;
    font-size: 23px; font-weight: 700; line-height: 30px;
  }
  .company-tagline {
    position: absolute; left: 136px; top: 448px;
    font-size: 21px; line-height: 28px;
  }
  .contact-row { position: absolute; left: 47px; right: 0; height: 60px; }
  .contact-row.phone { top: 520px; }
  .contact-row.email { top: 601px; }
  .contact-row.web { top: 682px; }
  .contact-icon {
    position: absolute; left: 0; top: 6px; width: 53px; height: 52px;
    border-radius: 5px; background: var(--accent-green);
    display: flex; align-items: center; justify-content: center;
  }
  .contact-value {
    position: absolute; left: 89px; top: 0; font-size: 23px; font-weight: 700; line-height: 30px;
    white-space: nowrap;
  }
  .contact-label {
    position: absolute; left: 89px; top: 36px; font-size: 23px; line-height: 30px;
  }
  .social-row {
    position: absolute; left: 34px; right: 34px; top: 808px;
    display: flex; justify-content: space-between; list-style: none;
  }
  .social-item {
    display: flex; align-items: center; gap: 6px;
    font-size: 13px; font-weight: 700; line-height: 30px;
  }
  .social-square {
    width: 16px; height: 16px; border: 2px solid var(--ink); border-radius: 3px;
  }
</style>
</head>
<body>
  <main class="card">
    <div class="earpiece-bar">
      <span class="camera-dot"></span>
      <span class="speaker-grille"></span>
    </div>

    <div class="status-bar">
      <div class="status-network">
        <svg width="32" height="16" viewBox="0 0 32 16" aria-hidden="true">
          <g fill="var(--ink)">
            <rect x="0" y="11" width="4" height="5"/><rect x="6" y="8" width="4" height="8"/>
            <rect x="12" y="5" width="4" height="11"/><rect x="18" y="2" width="4" height="14"/>
            <rect x="24" y="0" width="4" height="16"/>
          </g>
        </svg>
        <span>K-LUX</span>
        <svg width="24" height="20" viewBox="0 0 24 20" aria-hidden="true">
          <g fill="none" stroke="var(--ink)" stroke-width="2.6" stroke-linecap="round">
            <path d="M2 7a14 14 0 0 1 20 0"/><path d="M6 11a8.5 8.5 0 0 1 12 0"/>
          </g>
          <circle cx="12" cy="16" r="2.6" fill="var(--ink)"/>
        </svg>
      </div>
      <div class="status-time">09:00 PM</div>
      <div class="status-battery">
        <span>100%</span>
        <svg width="44" height="20" viewBox="0 0 44 20" aria-hidden="true">
          <rect x="1" y="2" width="38" height="16" rx="2" fill="none" stroke="var(--ink)" stroke-width="2"/>
          <rect x="4" y="5" width="32" height="10" fill="var(--ink)"/>
          <rect x="40" y="7" width="3" height="6" fill="var(--ink)"/>
        </svg>
      </div>
    </div>

    <h1 class="holder-name">Tomas Varga</h1>
    <p class="holder-title">Founder &amp; C.E.O</p>

    <p class="company-name">K-LUX Restaurant Marketing</p>
    <p class="company-tagline">Kindle Loyalty Using eXperience</p>

    <div class="contact-row phone">
      <span class="contact-icon">
        <svg width="30" height="30" viewBox="0 0 24 24" aria-hidden="true">
          <path fill="var(--white)" d="M6.6 10.8a15.2 15.2 0 0 0 6.6 6.6l2.2-2.2a1 1 0 0 1 1-.25 11.4 11.4 0 0 0 3.6.57 1 1 0 0 1 1 1V20a1 1 0 0 1-1 1A17 17 0 0 1 3 4a1 1 0 0 1 1-1h3.5a1 1 0 0 1 1 1c0 1.25.2 2.45.57 3.57a1 1 0 0 1-.25 1z"/>
        </svg>
      </span>
      <span class="contact-value">+1 (831) 555-0148</span>
      <span class="contact-label">Phone number</span>
    </div>

    <div class="contact-row email">
      <span class="contact-icon">
        <svg width="32" height="24" viewBox="0 0 32 24" aria-hidden="true">
          <rect x="2" y="3" width="28" height="18" fill="none" stroke="var(--white)" stroke-width="2"/>
          <path d="M2 3l14 11L30 3M2 21l10-9M30 21l-10-9" fill="none" stroke="var(--white)" stroke-width="2"/>
        </svg>
      </span>
      <span class="contact-value">tomas.varga1@postvale.com</span>
      <span class="contact-label">Email address</span>
    </div>

    <div class="contact-row web">
      <span class="contact-icon">
        <svg width="30" height="30" viewBox="0 0 30 30" aria-hidden="true">
          <g fill="none" stroke="var(--white)" stroke-width="2">
            <circle cx="15" cy="15" r="12"/>
            <ellipse cx="15" cy="15" rx="5.5" ry="12"/>
            <path d="M3 15h24M15 3v24M5 9h20M5 21h20"/>
          </g>
        </svg>
      </span>
      <span class="contact-value">www.kluxrestaurantmarketing.com</span>
      <span class="contact-label">Web address</span>
    </div>

    <ul class="social-row">
      <li class="social-item"><span class="social-square"></span>Pagebloom</li>
      <li class="social-item"><span class="social-square"></span>Picwell</li>
      <li class="social-item"><span class="social-square"></span>Quillet</li>
      <li class="social-item"><span class="social-square"></span>VexMo</li>
      <li class="social-item"><span class="social-square"></span>Streamora</li>
    </ul>

    <div class="home-bar">
      <span class="home-button"></span>
    </div>
  </main>
</body>
</html>
```